Quartz Pivot Business Card Design

I need a 2-sided business card for my computer engineering consulting company. The card is expected to convey a message of cutting edge forward thinking, and boldnes. I would like the card to be memorable and stand-out on a desk. The card should be bold, modern, clean, and highly professional. I am a big fan of watermarks/shadows and other intersting but restrained uses of the logo. The card can be a shape other than the traditional rectangle. Perhaps a rectangle with rounded edges. All I ask is the card be able to fit into a standard wallet. I will supply two logos, one with a red background, and one with a black background. Please feel free to work with both of these logos.
Updates

Hi all, thank you for your submissions. I will post the original vector file later today. Thank you for your patience.

Regards,

Martin

Target Market(s)

Engineering Buyers, Vice Presidents and Directors

Industry/Entity Type

Computer

Requirements
Must have
• 2 sides

```html
<!DOCTYPE html>
<html lang="en">
<head>
<meta charset="utf-8">
<title>Quartz Pivot Works – Business Card</title>
<link rel="stylesheet" href="https://fonts.googleapis.com/css2?family=Open+Sans:wght@400;600;700&display=swap">
<style>
  :root {
    --page-bg: #e9e6e1;
    --card-black: #060606;
    --card-grey: #555555;
    --band-grey: #5b5b5b;
    --brand-red: #c4161c;
    --text-white: #ffffff;
    --text-light: #e4e4e4;
  }
  * { box-sizing: border-box; margin: 0; padding: 0; }
  html, body { width: 1200px; height: 473px; overflow: hidden; }
  body {
    background: var(--page-bg);
    font-family: "Open Sans", Arial, sans-serif;
    position: relative;
  }
  .card {
    position: absolute;
    top: 83px;
    width: 526px;
    height: 299px;
    border-radius: 12px;
    overflow: hidden;
    box-shadow: 0 3px 10px rgba(0,0,0,0.25);
  }
  .card--front { left: 42px; background: var(--card-black); }
  .card--back { left: 611px; background: var(--card-grey); }

  .card__wave { position: absolute; inset: 0; }

  .brand { position: absolute; left: 0; right: 0; text-align: center; }
  .brand__mark {
    display: block;
    margin: 0 auto;
    background: var(--brand-red);
  }
  .brand__name {
    display: block;
    font-weight: 700;
    color: var(--brand-red);
    white-space: nowrap;
    letter-spacing: 0.3px;
  }

  .card--front .brand { top: 29px; }
  .card--front .brand__mark { width: 72px; height: 72px; }
  .card--front .brand__name { font-size: 24px; margin-top: 15px; line-height: 28px; }

  .holder {
    position: absolute;
    left: 0; right: 0; top: 208px;
    text-align: center;
    color: var(--text-white);
    font-size: 13px;
  }
  .holder__name { font-weight: 700; font-size: 16px; letter-spacing: 0.3px; }

  .contacts {
    position: absolute;
    left: 33px; top: 240px;
    display: flex;
    color: var(--text-light);
    font-size: 13.5px;
    line-height: 20px;
  }
  .contacts__col { padding: 0 8px; border-left: 1px solid var(--text-light); }
  .contacts__col:first-child { padding-left: 0; border-left: 0; }

  .logo-panel {
    position: absolute;
    left: 102px; top: 78px;
    width: 329px; height: 146px;
    background: var(--card-black);
  }
  .logo-panel .brand { top: 17px; }
  .logo-panel .brand__mark { width: 68px; height: 68px; }
  .logo-panel .brand__name { font-size: 23px; margin-top: 17px; line-height: 27px; }

  .website {
    position: absolute;
    left: 0; right: 0; top: 233px;
    text-align: center;
    color: var(--text-white);
    font-size: 13px;
    letter-spacing: 3px;
  }
</style>
</head>
<body>
  <section class="card card--front" aria-label="Card front">
    <svg class="card__wave" viewBox="0 0 526 299" aria-hidden="true">
      <path d="M0,152 C150,140 310,178 526,186 L526,299 L0,299 Z" fill="var(--brand-red)"/>
      <path d="M0,178 C170,166 330,188 526,195 L526,299 L0,299 Z" fill="var(--band-grey)"/>
    </svg>
    <div class="brand">
      <span class="brand__mark"></span>
      <span class="brand__name">QUARTZ PIVOT WORKS LTD</span>
    </div>
    <p class="holder"><span class="holder__name">YOUR NAME</span> Title</p>
    <div class="contacts">
      <div class="contacts__col">+91 12345 67890<br>+91 12345 67890</div>
      <div class="contacts__col">info@quartzpivot.com<br>www.quartzpivot.com</div>
      <div class="contacts__col">Complex Name, Street<br>City Name,000 000</div>
    </div>
  </section>

  <section class="card card--back" aria-label="Card back">
    <div class="logo-panel">
      <div class="brand">
        <span class="brand__mark"></span>
        <span class="brand__name">QUARTZ PIVOT WORKS LTD</span>
      </div>
    </div>
    <p class="website">www.quartzpivot.com</p>
  </section>
</body>
</html>
```